Step Boldly Toward Gain Promotional Flyer

I Need a one page, one-sided 8.5 x 11 editable promotional flyer that POPS!, designed in photoshop

[TITLE]Step Boldly Toward Gain: 3 BOLD Moves to Up-Level Your Business Now!

[CONTENT for the Flyer:]

At this content-rich event you will learn how to:
• Get out of feast and famine mode and into six, multi-six and/or seven figure-income mode
• Leapfrog your competition and become the obvious choice in your market
• Have your business aligned with who you are and what you want
• Enjoy your business far more than you imagined possible.
• Have more fun and time to yourself
• Live free and unbound!

Accolades
“Delphine helped us increase our six figure income by 41%...I feel reborn!” Marlene & Otis Pruitt, Vienna, VA

“…Delphine is a joy to listen to - compelling, smart, provocative…” – Dennis Ashcombe, Charlotte, North Carolina

“Delphine helped me increase my business by 66%...without me spending more time, money, or making cold calls! …I am in the zone!” Tina Worsley, Baltimore, MD
“Delphine is an energetic and dynamic speaker…content-rich…holds your attention to the very end!” Neil Barrow, Frmr Pres., Crane & Whitby, MD, MD, D.C., PA, DE, NJ
“Delphine is the real estate whisperer!” Hal Drummond, Washington D.C.

“Delphine was prepared, funny, informative and made a connection with each of our agents…Fabulous!…even my admins were PUMPED!!! – Paul Venable, New York

About Delphine:
Delphine is a highly regarded business development speaker & coach who knows how to pump up an audience and have them making more money, in less time, AND having more fun doing it! What’s not to love?! Consistently rated as an exceptional speaker and conference favorite! Among her work: Standout Method: How to Draw Your Best Buyers Time after Time!, Contact Sourcing Done Easy, The Worst Outreach Errors Real Estate Agents Commit and How to Steer Clear of Them, Slow Seasons Build Sharp Sellers, Drive Within the Head for Real Estate Agents.

[Also need a section for:]
Date: December 9, 2015, Time: 9:00 Am - 12:00 Noon, Place: Harbor Lantern Convention, Green Castle, PA

Target Market(s)

Real Estate Agents

Industry/Entity Type

Real Estate Agent

Font styles to use
Sans Serif

Colors
0655a3
f37122

Requirements
Must have
• the peak tier realty mentor logo
Nice to have
• step boldly toward gain logo; lots of POP! :-) ; open to other colors, accent colors.

```html
<!DOCTYPE html>
<html lang="en">
<head>
<meta charset="utf-8">
<title>Step Boldly Toward Gain – Event Flyer</title>
<link rel="stylesheet" href="https://fonts.googleapis.com/css2?family=Montserrat:wght@700;800;900&family=Roboto:ital,wght@0,400;0,700;1,400&display=swap">
<style>
  :root {
    --orange: #f37122;
    --navy: #0d1d4f;
    --ink: #111111;
    --grey-text: #8a8a8a;
    --panel: #e6e6e6;
    --white: #ffffff;
  }
  * { margin: 0; padding: 0; box-sizing: border-box; }
  html, body { width: 927px; height: 1200px; overflow: hidden; background: var(--white); }
  .flyer {
    position: relative; width: 927px; height: 1200px; overflow: hidden;
    font-family: "Roboto", Arial, sans-serif; color: var(--ink);
    background: radial-gradient(ellipse at 50% 30%, #ffffff 0%, #f1f1f1 60%, #dcdcdc 100%);
  }
  .abs { position: absolute; }

  .title {
    top: 58px; left: 0; width: 927px; text-align: center;
    font-family: "Montserrat", Arial, sans-serif; font-weight: 900; font-size: 49px;
    color: var(--orange); letter-spacing: 0.5px;
    text-shadow: 0 0 2px #fff, 2px 2px 4px rgba(0,0,0,.25);
  }
  .subtitle-small {
    top: 125px; left: 0; width: 927px; text-align: center;
    font-family: "Montserrat", Arial, sans-serif; font-weight: 800; font-size: 27px; color: var(--navy);
  }
  .subtitle-large {
    top: 157px; left: 0; width: 927px; text-align: center;
    font-family: "Montserrat", Arial, sans-serif; font-weight: 900; font-size: 41px; color: var(--navy);
    text-shadow: 1px 2px 3px rgba(0,0,0,.2);
  }
  .side-bar { top: 153px; right: 0; width: 34px; height: 257px; background: var(--orange); }

  .learn-heading {
    top: 240px; left: 55px; font-family: "Montserrat", Arial, sans-serif;
    font-weight: 800; font-size: 19px; color: var(--orange);
  }
  .learn-list { top: 278px; left: 52px; list-style: none; }
  .learn-list li {
    display: flex; align-items: center; height: 27.2px;
    font-weight: 700; font-size: 16.5px; color: var(--ink);
  }
  .learn-list .num {
    width: 17px; height: 17px; border-radius: 50%; background: var(--navy); color: var(--white);
    font-size: 10.5px; display: flex; align-items: center; justify-content: center; margin-right: 13px; flex: none;
  }

  .event-mark { top: 505px; left: 50px; display: flex; align-items: center; gap: 10px; }
  .event-mark .dot { width: 22px; height: 22px; border-radius: 50%; background: var(--orange); }
  .event-mark .name { font-weight: 700; font-size: 30px; color: var(--navy); }

  .coach-name {
    top: 402px; left: 420px; font-weight: 700; font-size: 37px; color: #9a9a9a;
  }
  .coach-mark { top: 455px; left: 360px; width: 330px; text-align: center; }
  .coach-mark .name { font-weight: 700; font-size: 42px; line-height: 46px; color: var(--orange); }

  .portrait {
    top: 322px; left: 662px; width: 265px; height: 300px;
    background: linear-gradient(180deg, #f2f2f2 0%, #d9c7b0 35%, #3a3a3a 80%, #1e1e1e 100%);
  }

  .band { top: 622px; left: 0; width: 927px; height: 258px; background: var(--orange); }
  .tagline-strip { top: 622px; left: 0; }
  .tagline {
    top: 642px; left: 245px; width: 682px; text-align: center;
    font-style: italic; font-size: 19px; color: var(--white);
  }

  .quotes { top: 698px; left: 24px; width: 880px; height: 155px; display: flex; }
  .quote {
    flex: 1; border-left: 1px solid rgba(255,255,255,.55); text-align: center;
    color: var(--white); font-style: italic; font-size: 14px; line-height: 17px; padding: 0 10px;
  }
  .quote:last-child { border-right: 1px solid rgba(255,255,255,.55); }
  .quote svg { display: block; margin: 4px auto 12px; }

  .about-edge { top: 880px; left: 0; width: 33px; height: 163px; background: var(--orange); }
  .about { top: 880px; left: 33px; width: 894px; height: 163px; background: var(--panel); padding: 26px 22px 0 22px; }
  .about h2 { font-weight: 700; font-size: 16px; text-decoration: underline; color: var(--ink); line-height: 17px; }
  .about p { font-size: 14px; line-height: 17.5px; color: var(--ink); text-align: justify; }

  .footer { top: 1043px; left: 0; width: 927px; height: 127px; background: var(--navy); }
  .footer-edge { top: 1170px; left: 0; width: 927px; height: 30px; background: var(--orange); }
  .divider { top: 1060px; left: 463px; width: 1px; height: 92px; background: rgba(255,255,255,.4); }
  .info-label {
    font-family: "Montserrat", Arial, sans-serif; font-weight: 800; font-size: 19px;
    color: var(--orange); text-decoration: underline;
  }
  .info-text { font-family: "Montserrat", Arial, sans-serif; font-weight: 700; font-size: 19px; color: var(--white); line-height: 24px; }
  .when { top: 1070px; left: 162px; }
  .where { top: 1070px; left: 610px; }
  .icon-clock { top: 1068px; left: 42px; }
  .icon-pin { top: 1064px; left: 508px; }
</style>
</head>
<body>
<div class="flyer">
  <h1 class="abs title">STEP BOLDLY TOWARD GAIN</h1>
  <p class="abs subtitle-small">3 BOLD MOVES TO</p>
  <p class="abs subtitle-large">UP-LEVEL YOUR BUSINESS NOW!</p>
  <div class="abs side-bar"></div>

  <h2 class="abs learn-heading">AT THIS CONTENT-RICH EVENT YOU WILL LEARN HOW TO:</h2>
  <ol class="abs learn-list">
    <li><span class="num">1</span>Get out of feast and famine mode and into six, multi-six and/or seven figure-income mode</li>
    <li><span class="num">2</span>Leapfrog your competition and become the obvious choice in your market</li>
    <li><span class="num">3</span>Have your business aligned with who you are and what you want</li>
    <li><span class="num">4</span>Enjoy your business far more than you imagined possible.</li>
    <li><span class="num">5</span>Have more fun and time to yourself</li>
    <li><span class="num">6</span>Live free and unbound!</li>
  </ol>

  <div class="abs event-mark"><span class="dot"></span><span class="name">Step Boldly Toward Gain</span></div>

  <div class="abs portrait" role="img" aria-label="Portrait photograph of coach Delphine Marlow"></div>
  <p class="abs coach-name">Delphine Marlow</p>
  <div class="abs coach-mark"><span class="name">Peak Tier Realty Mentor</span></div>

  <div class="abs band"></div>
  <svg class="abs tagline-strip" width="927" height="60" viewBox="0 0 927 60" aria-hidden="true">
    <polygon points="245,0 927,0 927,60 197,60" fill="var(--navy)"/>
  </svg>
  <p class="abs tagline">“America’s Peak Tier Realty Mentor” ™</p>

  <div class="abs quotes">
    <div class="quote">
      <svg width="50" height="42" viewBox="0 0 50 42" aria-hidden="true">
        <path d="M20 2c10 0 18 6 18 14s-8 14-18 14c-2 0-4 0-6-1l-9 5 3-8C4 23 2 20 2 16 2 8 10 2 20 2z" fill="none" stroke="#fff" stroke-width="3"/>
        <path d="M40 14c5 2 8 6 8 10 0 3-1 6-4 8l2 7-7-4c-2 1-4 1-6 1-6 0-11-2-14-6" fill="none" stroke="#fff" stroke-width="3"/>
        <circle cx="13" cy="16" r="2" fill="#fff"/><circle cx="20" cy="16" r="2" fill="#fff"/><circle cx="27" cy="16" r="2" fill="#fff"/>
      </svg>
      “Delphine helped us increase our six figure income by 41%...I feel reborn!”<br>Marlene &amp; Otis Pruitt,<br>Vienna, VA
    </div>
    <div class="quote">
      <svg width="50" height="42" viewBox="0 0 50 42" aria-hidden="true">
        <path d="M20 2c10 0 18 6 18 14s-8 14-18 14c-2 0-4 0-6-1l-9 5 3-8C4 23 2 20 2 16 2 8 10 2 20 2z" fill="none" stroke="#fff" stroke-width="3"/>
        <path d="M40 14c5 2 8 6 8 10 0 3-1 6-4 8l2 7-7-4c-2 1-4 1-6 1-6 0-11-2-14-6" fill="none" stroke="#fff" stroke-width="3"/>
        <circle cx="13" cy="16" r="2" fill="#fff"/><circle cx="20" cy="16" r="2" fill="#fff"/><circle cx="27" cy="16" r="2" fill="#fff"/>
      </svg>
      “…Delphine is a joy to listen to -<br>compelling, smart, provocative…”<br>Dennis Ashcombe, Charlotte,<br>North Carolina
    </div>
    <div class="quote">
      <svg width="50" height="42" viewBox="0 0 50 42" aria-hidden="true">
        <path d="M20 2c10 0 18 6 18 14s-8 14-18 14c-2 0-4 0-6-1l-9 5 3-8C4 23 2 20 2 16 2 8 10 2 20 2z" fill="none" stroke="#fff" stroke-width="3"/>
        <path d="M40 14c5 2 8 6 8 10 0 3-1 6-4 8l2 7-7-4c-2 1-4 1-6 1-6 0-11-2-14-6" fill="none" stroke="#fff" stroke-width="3"/>
        <circle cx="13" cy="16" r="2" fill="#fff"/><circle cx="20" cy="16" r="2" fill="#fff"/><circle cx="27" cy="16" r="2" fill="#fff"/>
      </svg>
      “Delphine was prepared, funny, informative and made a connection with each of our agents…Fabulous!…even my admins were PUMPED!!!”<br>Paul Venable,<br>New York
    </div>
  </div>

  <div class="abs about-edge"></div>
  <section class="abs about">
    <h2>ABOUT DELPHINE</h2>
    <p>Delphine is a highly regarded business development speaker &amp; coach who knows how to pump up an audience and have them making more money, in less time, AND having more fun doing it! What’s not to love?! Consistently rated as an exceptional speaker and conference favorite! Among her work: Standout Method: How to Draw Your Best Buyers Time after Time!, Contact Sourcing Done Easy, The Worst Outreach Errors Real Estate Agents Commit and How to Steer Clear of Them, Slow Seasons Build Sharp Sellers, Drive Within the Head for Real Estate Agents.</p>
  </section>

  <div class="abs footer"></div>
  <svg class="abs icon-clock" width="76" height="76" viewBox="0 0 76 76" aria-hidden="true">
    <circle cx="38" cy="38" r="33" fill="none" stroke="#fff" stroke-width="5"/>
    <path d="M38 16v22l-12 10" fill="none" stroke="#fff" stroke-width="5" stroke-linecap="round" stroke-linejoin="round"/>
    <circle cx="38" cy="38" r="3" fill="#fff"/>
  </svg>
  <div class="abs when">
    <div class="info-label">DATE &amp; TIME</div>
    <div class="info-text">December 9, 2015<br>9:00 Am - 12:00 Noon</div>
  </div>
  <div class="abs divider"></div>
  <svg class="abs icon-pin" width="66" height="86" viewBox="0 0 66 86" aria-hidden="true">
    <path d="M33 4c-13 0-23 10-23 23 0 17 23 41 23 41s23-24 23-41C56 14 46 4 33 4z" fill="none" stroke="#fff" stroke-width="5"/>
    <circle cx="33" cy="27" r="8" fill="none" stroke="#fff" stroke-width="5"/>
    <path d="M16 66c-9 2-12 5-12 8 0 5 13 8 29 8s29-3 29-8c0-3-3-6-12-8" fill="none" stroke="#fff" stroke-width="4"/>
  </svg>
  <div class="abs where">
    <div class="info-label">LOCATION</div>
    <div class="info-text">Harbor Lantern Convention,<br>Green Castle, PA</div>
  </div>
  <div class="abs footer-edge"></div>
</div>
</body>
</html>
```